Prickly Heat Powder

prickly heat powders are used in summers to provide cooling effect to body and relief body from heat effects during summers.

we have 4 variants of prickly heat.

1) Menthol
2) Rose
3) Lemon
4) Neem

Bottle is in round cylinder shape. It also has a cap. Will share pictures of bottle and cap tomorrow.

Brand Name is BRIVEL.

Total label size will be 180mm width * 140mm height. But main design will be small because bottle is round.

Target Market(s)

B Class.
C plus and C.
Masses

Industry/Entity Type

Cosmetics

Requirements
Must have
• icy effect, joyful and playful
Nice to have
• joyful and eye catching designs. more colors would be good.
• Polar bear might look nice.
• Brivel Logo to be bold and prominent.

```html
<!DOCTYPE html>
<html lang="en">
<head>
<meta charset="utf-8">
<title>Brivel Prickly Heat Powder – Label Range</title>
<link rel="stylesheet" href="https://fonts.googleapis.com/css2?family=PT+Sans+Narrow:wght@400;700&display=swap">
<style>
  :root {
    --page-bg: #ececec;
    --band-blue: #2f3f9e;
    --band-blue-light: #4a63c9;
    --silver: #b9bcc2;
    --silver-light: #f2f3f5;
    --text-white: #ffffff;
    --menthol: #3dbb7a;
    --menthol-light: #bfe6d2;
    --rose: #f07fa8;
    --rose-light: #fde0ea;
    --lemon: #f0d26e;
    --lemon-light: #fbf2cf;
    --ice: #dfe8f2;
    --ice-deep: #9fb3c9;
  }
  html, body {
    margin: 0;
    padding: 0;
    width: 1200px;
    height: 1200px;
    overflow: hidden;
    background: var(--page-bg);
    font-family: "PT Sans Narrow", "Arial Narrow", sans-serif;
  }
  .label-range {
    position: absolute;
    left: 155px;
    top: 290px;
    display: flex;
    gap: 70px;
  }
  .label {
    width: 250px;
    height: 620px;
    display: block;
    box-shadow: 0 6px 18px rgba(0,0,0,0.12);
  }
  .brand-name {
    font-family: "PT Sans Narrow", "Arial Narrow", sans-serif;
    font-weight: 700;
    font-size: 56px;
    fill: var(--text-white);
    letter-spacing: 1px;
  }
  .product-type {
    font-family: "PT Sans Narrow", "Arial Narrow", sans-serif;
    font-weight: 400;
    font-size: 17px;
    fill: var(--text-white);
    letter-spacing: 0.5px;
  }
  .variant-name {
    font-family: "PT Sans Narrow", "Arial Narrow", sans-serif;
    font-weight: 400;
    font-size: 32px;
    fill: var(--text-white);
  }
  .band-silver { fill: url(#silverGrad); }
  .band-blue { fill: url(#blueGrad); }
  .band-grey { fill: #9a9ea6; }
</style>
</head>
<body>
<svg width="0" height="0" style="position:absolute" aria-hidden="true">
  <defs>
    <linearGradient id="silverGrad" x1="0" y1="0" x2="1" y2="0">
      <stop offset="0" stop-color="#8e9299"/>
      <stop offset="0.5" stop-color="#f2f3f5"/>
      <stop offset="1" stop-color="#8e9299"/>
    </linearGradient>
    <linearGradient id="blueGrad" x1="0" y1="0" x2="1" y2="0">
      <stop offset="0" stop-color="#2f3f9e"/>
      <stop offset="0.55" stop-color="#4a63c9"/>
      <stop offset="1" stop-color="#2f3f9e"/>
    </linearGradient>
    <radialGradient id="iceGrad" cx="0.5" cy="0.55" r="0.6">
      <stop offset="0" stop-color="#f4f8fc"/>
      <stop offset="0.6" stop-color="#c9d6e4"/>
      <stop offset="1" stop-color="#c9d6e4" stop-opacity="0"/>
    </radialGradient>
    <radialGradient id="mentholBg" cx="0.4" cy="0.05" r="0.9">
      <stop offset="0" stop-color="#bfe6d2"/>
      <stop offset="0.5" stop-color="#3dbb7a"/>
    </radialGradient>
    <radialGradient id="roseBg" cx="0.5" cy="0.05" r="0.9">
      <stop offset="0" stop-color="#fde0ea"/>
      <stop offset="0.5" stop-color="#f07fa8"/>
    </radialGradient>
    <radialGradient id="lemonBg" cx="0.4" cy="0.05" r="0.9">
      <stop offset="0" stop-color="#fbf2cf"/>
      <stop offset="0.5" stop-color="#f0d26e"/>
    </radialGradient>
    <radialGradient id="mintSpot" cx="0.5" cy="0.5" r="0.5">
      <stop offset="0" stop-color="#4fb83e"/>
      <stop offset="1" stop-color="#4fb83e" stop-opacity="0"/>
    </radialGradient>
    <radialGradient id="roseSpot" cx="0.5" cy="0.5" r="0.5">
      <stop offset="0" stop-color="#e43a7c"/>
      <stop offset="1" stop-color="#e43a7c" stop-opacity="0"/>
    </radialGradient>
    <radialGradient id="lemonSpot" cx="0.5" cy="0.5" r="0.5">
      <stop offset="0" stop-color="#f7b81c"/>
      <stop offset="1" stop-color="#f7b81c" stop-opacity="0"/>
    </radialGradient>
  </defs>
</svg>

<main class="label-range">
  <!-- Menthol -->
  <svg class="label label--menthol" viewBox="0 0 250 620" xmlns="http://www.w3.org/2000/svg">
    <rect width="250" height="620" fill="url(#mentholBg)"/>
    <polygon class="band-silver" points="0,112 250,82 250,170 0,200"/>
    <polygon class="band-blue" points="0,120 250,90 250,158 0,188"/>
    <text class="brand-name" x="125" y="160" text-anchor="middle">BRIVEL</text>
    <polygon class="band-grey" points="0,200 250,170 250,196 0,226"/>
    <text class="product-type" x="125" y="205" text-anchor="middle">PRICKLY HEAT POWDER</text>
    <g role="img" aria-label="Ice cubes with icy splash and fresh mint leaves">
      <rect x="0" y="226" width="250" height="270" fill="url(#iceGrad)"/>
      <ellipse cx="130" cy="430" rx="70" ry="55" fill="url(#mintSpot)"/>
    </g>
    <polygon class="band-silver" points="0,500 250,460 250,565 0,600"/>
    <polygon class="band-blue" points="0,508 250,468 250,555 0,590"/>
    <text class="variant-name" x="225" y="548" text-anchor="end">MENTHOL</text>
  </svg>

  <!-- Rose -->
  <svg class="label label--rose" viewBox="0 0 250 620" xmlns="http://www.w3.org/2000/svg">
    <rect width="250" height="620" fill="url(#roseBg)"/>
    <polygon class="band-silver" points="0,112 250,82 250,170 0,200"/>
    <polygon class="band-blue" points="0,120 250,90 250,158 0,188"/>
    <text class="brand-name" x="125" y="160" text-anchor="middle">BRIVEL</text>
    <polygon class="band-grey" points="0,200 250,170 250,196 0,226"/>
    <text class="product-type" x="125" y="205" text-anchor="middle">PRICKLY HEAT POWDER</text>
    <g role="img" aria-label="Ice cubes with icy splash and a pink rose bloom">
      <rect x="0" y="226" width="250" height="270" fill="url(#iceGrad)"/>
      <ellipse cx="135" cy="430" rx="72" ry="58" fill="url(#roseSpot)"/>
    </g>
    <polygon class="band-silver" points="0,500 250,460 250,565 0,600"/>
    <polygon class="band-blue" points="0,508 250,468 250,555 0,590"/>
    <text class="variant-name" x="210" y="548" text-anchor="end">ROSE</text>
  </svg>

  <!-- Lemon -->
  <svg class="label label--lemon" viewBox="0 0 250 620" xmlns="http://www.w3.org/2000/svg">
    <rect width="250" height="620" fill="url(#lemonBg)"/>
    <polygon class="band-silver" points="0,112 250,82 250,170 0,200"/>
    <polygon class="band-blue" points="0,120 250,90 250,158 0,188"/>
    <text class="brand-name" x="125" y="160" text-anchor="middle">BRIVEL</text>
    <polygon class="band-grey" points="0,200 250,170 250,196 0,226"/>
    <text class="product-type" x="125" y="205" text-anchor="middle">PRICKLY HEAT POWDER</text>
    <g role="img" aria-label="Ice cubes with icy splash and a whole and halved lemon">
      <rect x="0" y="226" width="250" height="270" fill="url(#iceGrad)"/>
      <ellipse cx="150" cy="425" rx="85" ry="55" fill="url(#lemonSpot)"/>
    </g>
    <polygon class="band-silver" points="0,500 250,460 250,565 0,600"/>
    <polygon class="band-blue" points="0,508 250,468 250,555 0,590"/>
    <text class="variant-name" x="220" y="548" text-anchor="end">LEMON</text>
  </svg>
</main>
</body>
</html>
```